The Copper Fellow Mo Wax Label

Hi Chaps,

We are needing a lable for our new moustache wax.

The design needs to be on a circular label. the size of the label is 32mm in diameter.

It needs to align with our branding from our beard oil product. checkout www.thecopperfellow-demo.com to get an insight of this.

what needs to be on the label:

- The copper fellow logo (please pull from website, will send through hi def image when design is selected)
- Fine Grain Moustache Wax
- the word "soft/medium hold"

This project will be open for 48 hours.

Any questions, please ask asap.
Updates

Our Logo and fonts that we use for our brand are now attached to the brief. 

Industry/Entity Type

Product

Requirements
Must have
• Must have
The copper fellow logo (please pull from website, will send through hi def image when design is selected)
- Fine Grain Moustache Wax
- allign with branding
- actual size 32mm diameter

```html
<!DOCTYPE html>
<html lang="en">
<head>
<meta charset="utf-8">
<title>The Copper Fellow – Moustache Wax Label</title>
<link href="https://fonts.googleapis.com/css2?family=Alfa+Slab+One&display=swap" rel="stylesheet">
<style>
  :root {
    --backdrop: #f2f2f4;
    --label: #ffffff;
    --ink: #111111;
  }
  html, body {
    margin: 0;
    padding: 0;
    width: 1200px;
    height: 1000px;
    overflow: hidden;
    background: var(--backdrop);
  }
  .label {
    display: block;
    width: 1200px;
    height: 1000px;
  }
  .label-face { fill: var(--label); stroke: var(--ink); stroke-width: 4; }
  .dot-ring { fill: none; stroke: var(--ink); stroke-width: 4.5; stroke-linecap: round; stroke-dasharray: 0 9.4; }
  .inner-rim { fill: none; stroke: var(--ink); stroke-width: 4; }
  .side-rule { fill: none; stroke: var(--ink); stroke-width: 4; }
  .curved-title, .hold-strength {
    font-family: "Alfa Slab One", Georgia, serif;
    font-size: 37px;
    letter-spacing: 2px;
    fill: var(--ink);
  }
  .brand-name {
    font-family: "Alfa Slab One", Georgia, serif;
    font-size: 40px;
    fill: var(--ink);
  }
  .brand-dot { fill: var(--ink); }
</style>
</head>
<body>
<svg class="label" viewBox="0 0 1200 1000" xmlns="http://www.w3.org/2000/svg">
  <defs>
    <path id="title-arc" d="M 373 511 A 228 228 0 0 1 829 511"/>
    <path id="hold-arc" d="M 377 511 A 224 224 0 0 0 825 511"/>
  </defs>

  <circle class="label-face" cx="601" cy="511" r="348"/>
  <circle class="dot-ring" cx="601" cy="511" r="337"/>
  <circle class="dot-ring" cx="601" cy="511" r="327"/>
  <circle class="dot-ring" cx="601" cy="511" r="317"/>
  <circle class="inner-rim" cx="601" cy="511" r="306"/>

  <path class="side-rule" d="M 361 440 A 250 250 0 0 0 428 691"/>
  <path class="side-rule" d="M 841 440 A 250 250 0 0 1 774 691"/>

  <text class="curved-title"><textPath href="#title-arc" startOffset="50%" text-anchor="middle">FINE GRAIN MOUSTACHE WAX</textPath></text>
  <text class="hold-strength" dy="30"><textPath href="#hold-arc" startOffset="50%" text-anchor="middle">MEDIUM HOLD</textPath></text>

  <g class="brand-mark" role="img" aria-label="The Copper Fellow brand name">
    <circle class="brand-dot" cx="601" cy="440" r="14"/>
    <text class="brand-name" x="601" y="510" text-anchor="middle">THE COPPER</text>
    <text class="brand-name" x="601" y="560" text-anchor="middle">FELLOW</text>
  </g>
</svg>
</body>
</html>
```